Valtren Power Core Values Poster

We want to display our company core values around our business. we want a poster that lists them with some cool solar graphics attached. This is to inspire and motivate our employees, promote our company and continue to adhere to a high code of conduct.

kladsf al asa kajdlkj akdj afa sdlkdjalk a dj faklsdoejsd poj dfoperjeo aod sd oe e oeoee fr oeoeo oee oeoeoe eooeoeoe eoeoeoeododoeoo dd d od d o d dddo doododo do dodododo do do doododo dodo odododododo dododoododododododododood ododo dododo

Target Market(s)

Employees

Industry/Entity Type

Solar Energy

Font styles to use
Serif

Colors
3176b5

Requirements
Must have
• All of the listed content in core values document. Can be multiple posters
Nice to have
• inspirational pictures
Should not have
• N/A

```html
<!DOCTYPE html>
<html lang="en">
<head>
<meta charset="utf-8">
<title>Valtren Power – Mission, Vision &amp; Core Values</title>
<link href="https://fonts.googleapis.com/css2?family=Roboto+Slab:wght@400;600;700;800&display=swap" rel="stylesheet">
<style>
  :root {
    --brand-blue: #3176b5;
    --sky-top: #2f5f9f;
    --sky-mid: #6f9acb;
    --sky-low: #b9cde3;
    --horizon: #e9d2ae;
    --sunset: #d9a86e;
    --ground: #2b2a24;
    --text-light: #ffffff;
    --photo-tone-a: #7f8e9c;
    --photo-tone-b: #b6bcc0;
  }
  * { margin: 0; padding: 0; box-sizing: border-box; }
  html, body { width: 900px; height: 1200px; overflow: hidden; }
  body { font-family: "Roboto Slab", Georgia, serif; background: #ffffff; }

  .poster {
    position: relative;
    width: 900px;
    height: 1200px;
    overflow: hidden;
    color: var(--text-light);
  }
  .poster__backdrop {
    position: absolute; inset: 0;
    background: linear-gradient(180deg,
      var(--sky-top) 0%,
      var(--sky-mid) 38%,
      var(--sky-low) 66%,
      #dfe5ea 78%,
      var(--horizon) 84%,
      var(--sunset) 87%,
      #5a4a36 90%,
      var(--ground) 93%,
      var(--ground) 100%);
  }

  .mission {
    position: absolute; top: 34px; left: 20px; right: 20px;
    text-align: center;
  }
  .mission__title {
    font-size: 60px; font-weight: 700; letter-spacing: 1px; line-height: 1.1;
  }
  .mission__text {
    margin-top: 8px;
    font-size: 32px; font-weight: 700; line-height: 45px;
  }

  .vision {
    position: absolute; top: 292px; left: 40px; width: 288px;
    text-align: right;
    font-size: 23px; line-height: 33px; font-weight: 600;
  }
  .section-title {
    font-size: 27px; font-weight: 800; line-height: 36px; white-space: nowrap;
  }

  .crew-photo {
    position: absolute; top: 291px; left: 354px; width: 201px; height: 279px;
    background: linear-gradient(160deg, var(--photo-tone-b) 0%, var(--photo-tone-a) 55%, #5f6b72 100%);
  }

  .core-values {
    position: absolute; top: 292px; left: 579px; width: 310px;
    font-size: 23px; line-height: 33px; font-weight: 600;
    white-space: nowrap;
  }
  .value { margin-bottom: 10px; }
  .value__name { font-weight: 800; }

  .brand {
    position: absolute; top: 938px; left: 570px; width: 310px;
    font-size: 38px; font-weight: 700; line-height: 1; white-space: nowrap;
    color: var(--brand-blue);
  }
</style>
</head>
<body>
  <main class="poster">
    <div class="poster__backdrop" role="img" aria-label="Photograph of a clear blue sky fading to a sunset horizon over a solar carport in a field"></div>

    <header class="mission">
      <h1 class="mission__title">MISSION</h1>
      <p class="mission__text">Provide our customers with the highest quality,<br>renewable energy products and services to maximize<br>their savings and give them the freedom to power<br>anything, anywhere.</p>
    </header>

    <section class="vision">
      <h2 class="section-title">VISION:</h2>
      <p>Continue to be<br>a full service<br>renewable energy<br>company providing<br>solar, battery storage,<br>off-grid, service,<br>and maintenance<br>solutions.</p>
    </section>

    <div class="crew-photo" role="img" aria-label="Photograph of installers in safety vests and hard hats working on a rooftop solar array"></div>

    <section class="core-values">
      <h2 class="section-title">CORE VALUES:</h2>
      <p class="value"><span class="value__name">INTEGRITY</span> – Do the<br>right thing.</p>
      <p class="value"><span class="value__name">QUALITY</span> – Provide<br>excellent components<br>and construction<br>that stand the test of<br>time.</p>
      <p class="value"><span class="value__name">SERVICE</span> – Meet the<br>customer' needs<br>today, tomorrow, and<br>for life.</p>
      <p class="value"><span class="value__name">VALUE</span> – The most<br>savings for the<br>money.</p>
    </section>

    <div class="brand">Valtren Power</div>
  </main>
</body>
</html>
```